Call center Word Template for Business Proposals

We recently opened a Call Center that handles the customer service for financial institutions. We just got our logo and we need a Word template for our business proposals, this way we can make them look very professional. I am attaching all the files with our logo that may be needed.

Target Market(s)

Financial institutions

Industry/Entity Type

Call Center

Font styles to use
Serif
Sans Serif

Colors
0d5aa7
3176b5
85acd3
cedeed
eaf1f7
feeeee
fbd4d5
f59195
f04a50

Requirements
Nice to have
• Sleek modern design

```html
<!DOCTYPE html>
<html lang="en">
<head>
<meta charset="utf-8">
<title>Norvale Proposal Templates</title>
<link href="https://fonts.googleapis.com/css2?family=Montserrat:wght@500&display=swap" rel="stylesheet">
<style>
  :root {
    --backdrop: #ececec;
    --brand-blue: #074f96;
    --brand-red: #e8202a;
    --soft-red: #e3444c;
    --navy: #00243f;
    --paper: #ffffff;
    --mist: #f4f4f4;
    --fog: #d6d6d6;
  }
  html, body {
    margin: 0;
    padding: 0;
    overflow: hidden;
  }
  .canvas {
    position: relative;
    width: 1200px;
    height: 959px;
    background: var(--backdrop);
    overflow: hidden;
  }
  .page {
    position: absolute;
    top: 152px;
    width: 507px;
    height: 669px;
    display: block;
  }
  .page--cover { left: 68px; }
  .page--letter { left: 626px; }
  .brand-name {
    font-family: "Montserrat", sans-serif;
    font-weight: 500;
    font-size: 22px;
    letter-spacing: 6px;
    fill: var(--paper);
  }
</style>
</head>
<body>
<main class="canvas">

  <svg class="page page--cover" viewBox="0 0 571 754" aria-label="Proposal cover page">
    <rect class="sheet" width="571" height="754" fill="var(--paper)"/>
    <polygon class="band-mist" points="0,163 243,93 395,182 571,131 571,392 230,160 0,270" fill="var(--mist)"/>
    <polygon class="band-fog" points="175,110 395,182 571,131 410,252" fill="var(--fog)" opacity="0.7"/>
    <polygon class="corner-red" points="0,0 87,0 243,93 0,163" fill="var(--soft-red)"/>
    <polygon class="header-blue" points="87,0 571,0 571,131 395,182 243,93" fill="var(--brand-blue)"/>
    <circle class="brand-dot" cx="340" cy="102" r="6" fill="var(--paper)"/>
    <text class="brand-name" x="356" y="110">NORVALE</text>
  </svg>

  <svg class="page page--letter" viewBox="0 0 571 754" aria-label="Proposal letter page">
    <rect class="frame-blue" width="571" height="754" fill="var(--brand-blue)"/>
    <polygon class="content-panel" points="28,148 297,148 350,37 544,37 544,629 358,675 163,604 28,657" fill="var(--paper)"/>
    <polygon class="panel-shade" points="350,37 544,37 544,270 380,37" fill="var(--mist)"/>
    <polygon class="glass-band" points="0,520 358,675 571,592 571,640 358,700 0,560" fill="var(--paper)" opacity="0.12"/>
    <polygon class="base-red" points="0,676 177,646 485,754 0,754" fill="var(--brand-red)"/>
    <polygon class="base-navy" points="358,675 571,629 571,754" fill="var(--navy)"/>
    <circle class="brand-dot" cx="60" cy="105" r="6" fill="var(--paper)"/>
    <text class="brand-name" x="76" y="113">NORVALE</text>
  </svg>

</main>
</body>
</html>
```